Gentle Harbor Label

We need labels for a new brewery called "Gentle Harbor":

We need one label, that we can slightly change to suit the style of liquid. So far the beers are:
- XPA
- Pale ALe
- IPA
- Black Ale

We want creative, fun labels, nothing traditional. but appropriate to suit all international markets.

Design was promoted in LOGO & not in Design, so we got a lot of logo's but very little designs for bottles/cans.

Gentle Harbor Brewing

```html
<!DOCTYPE html>
<html lang="en">
<head>
<meta charset="utf-8">
<title>Gentle Harbor Brewing – Bottle Label</title>
<link href="https://fonts.googleapis.com/css2?family=Cinzel:wght@600&display=swap" rel="stylesheet">
<style>
  :root {
    --canvas-bg: #ffffff;
    --label-black: #141210;
    --band-black: #1f1d1c;
    --gold-pale: #f7e9bd;
    --gold-light: #eed38c;
    --gold-mid: #d9b866;
    --gold-deep: #a9853a;
    --name-gold: #f0d27e;
  }
  html, body {
    margin: 0;
    padding: 0;
    width: 1200px;
    height: 1000px;
    overflow: hidden;
    background: var(--canvas-bg);
  }
  .canvas {
    position: relative;
    width: 1200px;
    height: 1000px;
    background: var(--canvas-bg);
  }
  .label {
    position: absolute;
    left: 360px;
    top: 50px;
    width: 480px;
    height: 900px;
    background: var(--label-black);
    overflow: hidden;
    border-radius: 4px;
  }
  .flourish-pattern {
    position: absolute;
    left: 0;
    width: 480px;
    z-index: 1;
  }
  .flourish-pattern--top {
    top: 0;
    height: 290px;
    background: linear-gradient(135deg,
      var(--gold-pale) 0%, var(--gold-light) 22%, var(--label-black) 38%,
      var(--gold-mid) 55%, var(--label-black) 72%, var(--gold-light) 88%, var(--gold-pale) 100%);
  }
  .flourish-pattern--bottom {
    top: 540px;
    height: 360px;
    background: linear-gradient(45deg,
      var(--gold-pale) 0%, var(--gold-light) 18%, var(--label-black) 34%,
      var(--gold-mid) 52%, var(--label-black) 68%, var(--gold-light) 86%, var(--gold-pale) 100%);
  }
  .name-band {
    position: absolute;
    left: 0;
    top: 250px;
    width: 480px;
    height: 360px;
    z-index: 2;
  }
  .name-band svg {
    position: absolute;
    inset: 0;
  }
  .brand-name {
    position: absolute;
    left: 0;
    right: 0;
    top: 118px;
    text-align: center;
    font-family: "Cinzel", serif;
    font-weight: 600;
    color: var(--name-gold);
    line-height: 1.05;
    margin: 0;
  }
  .brand-name__main {
    display: block;
    font-size: 50px;
    letter-spacing: 1px;
  }
  .brand-name__sub {
    display: block;
    font-size: 26px;
    letter-spacing: 3px;
    margin-top: 6px;
  }
</style>
</head>
<body>
<div class="canvas">
  <div class="label">
    <div class="flourish-pattern flourish-pattern--top" role="img" aria-label="Gold baroque flourish pattern on black"></div>

    <div class="name-band">
      <svg width="480" height="360" viewBox="0 0 480 360" aria-hidden="true">
        <path d="M0 34 Q240 0 480 34 L480 296 Q320 292 240 338 Q160 292 0 296 Z" fill="var(--band-black)"/>
        <path d="M0 26 Q240 -8 480 26" fill="none" stroke="var(--gold-mid)" stroke-width="3"/>
        <path d="M0 38 Q240 4 480 38" fill="none" stroke="var(--gold-deep)" stroke-width="1.5"/>
        <path d="M0 290 Q160 286 240 330 Q320 286 480 290" fill="none" stroke="var(--gold-deep)" stroke-width="1.5"/>
        <path d="M0 302 Q160 298 240 344 Q320 298 480 302" fill="none" stroke="var(--gold-mid)" stroke-width="3"/>
      </svg>
      <p class="brand-name">
        <span class="brand-name__main">Gentle Harbor</span>
        <span class="brand-name__sub">Brewing</span>
      </p>
    </div>

    <div class="flourish-pattern flourish-pattern--bottom" role="img" aria-label="Gold baroque flourish pattern on black"></div>
  </div>
</div>
</body>
</html>
```